Varden Chiropractic Business Cards

[Front]
[FLX/Stonerunner LOGO & Varden Chiropractic LOGO]
Neck & Back Pain Relief
Dr. Marcus Varden
Doctor of Chiropractic

• Short Term Care For Your Neck & Back Pain
• No Referral Needed
• Affordable / Insurance Accepted
• Proficient in treating Soft Tissue Problems

[Back]
For Valuable Wellness Inbox Notes™ Emailed To You Free, Go To:
www.DrMarcusVardenJournal.example
[SpinaGuard LOGO] - can be small

OFFICE HOURS:
Monday – Thursday
9 am - 12 noon, 2 pm - 6 pm
WALK-INS WELCOME

Industry/Entity Type

Business

Contact Information for Business Card

Varden Chiropractic Center, PLLC
4387 Talbrook Avenue, Suite K
Ashford Mill, NC 27999
(252) 555-0147
www.vardenchiro.example

Requirements
Must have
• The FLX/Stonerunner Logo
The Varden Chiropractic Logo
Should not have
• A picture of a spine

```html
<!DOCTYPE html>
<html lang="en">
<head>
<meta charset="utf-8">
<title>Varden Chiropractic Business Cards</title>
<link rel="stylesheet" href="https://fonts.googleapis.com/css2?family=Cabin:wght@500&family=PT+Sans:wght@400;700&display=swap">
<style>
  :root {
    --backdrop: #7a5c3c;
    --card: #46586f;
    --card-light: #53667f;
    --white: #ffffff;
    --ink: #1f2a38;
    --band: #121212;
    --accent: #3fa6dd;
    --badge: #2a2a2a;
  }
  * { margin: 0; padding: 0; box-sizing: border-box; }
  html, body { width: 996px; height: 1200px; overflow: hidden; }
  body {
    background: var(--backdrop);
    font-family: "PT Sans", sans-serif;
    color: var(--white);
    position: relative;
  }
  .card {
    position: absolute;
    width: 786px;
    height: 448px;
    background: linear-gradient(160deg, var(--card-light), var(--card) 60%);
    overflow: hidden;
  }
  .card-front { left: 119px; top: 131px; }
  .card-back { left: 107px; top: 606px; }

  .brand-plate {
    position: absolute; left: 34px; top: 25px; width: 287px; height: 107px;
    background: var(--white);
    display: flex; align-items: center; justify-content: center; gap: 10px;
  }
  .brand-mark { width: 18px; height: 18px; border-radius: 50%; background: var(--accent); }
  .brand-name { color: var(--ink); font-size: 25px; font-weight: 400; letter-spacing: 0.5px; }

  .partner-plate {
    position: absolute; left: 352px; top: 90px; width: 246px; height: 43px;
    background: var(--badge); border-radius: 3px;
    display: flex; align-items: center; justify-content: center;
    font-size: 17px; font-weight: 700; color: var(--white); letter-spacing: 0.5px;
  }

  .headline {
    position: absolute; left: 32px; top: 168px;
    font-family: "Cabin", sans-serif; font-weight: 500;
    font-size: 41px; letter-spacing: 0.5px; line-height: 1;
  }
  .benefits {
    position: absolute; left: 34px; top: 229px;
    list-style: none; font-size: 18px; line-height: 28.5px;
  }
  .benefits li::before { content: "• "; }
  .benefits li:nth-child(even) { padding-left: 4px; }

  .doctor {
    position: absolute; right: 27px; top: 236px; text-align: right;
  }
  .doctor-name { font-size: 23px; font-weight: 700; line-height: 30px; }
  .doctor-title { font-size: 21px; line-height: 30px; }

  .divider {
    position: absolute; left: 20px; right: 20px; top: 348px; height: 2px;
    background: linear-gradient(90deg, transparent, rgba(255,255,255,0.7) 40%, rgba(255,255,255,0.8) 80%, transparent);
  }
  .contact {
    position: absolute; right: 27px; top: 364px;
    display: flex; align-items: center; gap: 8px; font-size: 18px;
  }
  .contact svg { width: 16px; height: 16px; }

  .address-band {
    position: absolute; left: 0; right: 0; bottom: 0; height: 54px;
  }
  .address-band .teeth {
    height: 12px;
    background:
      linear-gradient(-45deg, var(--band) 6px, transparent 0),
      linear-gradient(45deg, var(--band) 6px, transparent 0);
    background-size: 12px 12px;
    background-repeat: repeat-x;
    background-position: left bottom;
  }
  .address-band .bar {
    height: 42px; background: var(--band);
    display: flex; align-items: center; justify-content: center;
    font-size: 17px; white-space: nowrap;
  }

  .newsletter {
    position: absolute; left: 46px; top: 30px; font-size: 20px; line-height: 40px;
  }
  .newsletter-url { font-weight: 700; font-size: 21px; }
  .trust-name {
    position: absolute; left: 46px; top: 160px;
    font-size: 31px; font-weight: 700; letter-spacing: 0.3px;
  }
  .hours { position: absolute; left: 42px; top: 262px; }
  .hours-title { font-size: 23px; font-weight: 700; line-height: 26px; }
  .hours-days, .hours-times { font-size: 21px; line-height: 30px; }
  .walk-ins { position: absolute; left: 42px; top: 383px; font-size: 23px; }

  .brand-accent {
    position: absolute; right: 90px; top: 95px; width: 230px; height: 230px;
    border-radius: 50%;
    background: radial-gradient(circle at 40% 40%, rgba(63,166,221,0.55), rgba(63,166,221,0.15));
  }
</style>
</head>
<body>

  <section class="card card-front" aria-label="Business card front">
    <div class="brand-plate">
      <span class="brand-mark"></span>
      <span class="brand-name">Varden Chiropractic</span>
    </div>
    <div class="partner-plate">FLX / Stonerunner</div>

    <h1 class="headline">NECK &amp; BACK PAIN RELIEF</h1>
    <ul class="benefits">
      <li>Short Term Care For Your Neck &amp; Back Pain</li>
      <li>No Referral Needed</li>
      <li>Affordable / Insurance Accepted</li>
      <li>Proficient in treating Soft Tissue Problems</li>
    </ul>

    <div class="doctor">
      <p class="doctor-name">Dr. Marcus Varden</p>
      <p class="doctor-title">Doctor of Chiropractic</p>
    </div>

    <div class="divider"></div>

    <div class="contact">
      <svg viewBox="0 0 16 16" aria-hidden="true"><path fill="#fff" d="M4 1h3l1 4-2 1.5c.8 1.8 2 3 3.5 3.5L11 8l4 1v3c0 1-1 2-2 2C7 14 2 9 2 3c0-1 1-2 2-2z"/></svg>
      <span>(252) 555-0147</span>
      <svg viewBox="0 0 16 16" aria-hidden="true"><g fill="none" stroke="#fff" stroke-width="1.3"><circle cx="8" cy="8" r="6.5"/><ellipse cx="8" cy="8" rx="2.8" ry="6.5"/><path d="M1.5 8h13M2.5 4.8h11M2.5 11.2h11"/></g></svg>
      <span>www.vardenchiro.example</span>
    </div>

    <div class="address-band">
      <div class="teeth"></div>
      <div class="bar">Varden Chiropractic Center, PLLC 4387 Talbrook Avenue, Suite K Ashford Mill, NC 27999</div>
    </div>
  </section>

  <section class="card card-back" aria-label="Business card back">
    <div class="newsletter">
      <p>For Valuable Wellness Inbox Notes™</p>
      <p>Emailed To You Free, Go To:</p>
      <p class="newsletter-url">www.DrMarcusVardenJournal.example</p>
    </div>
    <p class="trust-name">SpinaGuard</p>

    <div class="hours">
      <p class="hours-title">OFFICE HOURS:</p>
      <p class="hours-days">Monday – Thursday:</p>
      <p class="hours-times">9 am - 12 noon, 2 pm - 6 pm</p>
    </div>
    <p class="walk-ins">WALK-INS WELCOME</p>

    <div class="brand-accent" role="img" aria-label="Varden Chiropractic brand accent"></div>
  </section>

</body>
</html>
```